Commercial photographer, UAV drone photography & 360 walk-through visuals

I need a business card design that is minimalist but yet pretentiously creative. My target market are architects, designers, advertising agents and marketing managers. It is important to stress that though I am asking for a minimalist design it needs to have creative impact.

Target Market(s)

Architects, interiors designers, web-designers, artists

Contact Information for Business Card

Include my name, mobile [cell] number, email, web page and the company logo. Do not to include a postal address.

Colors

Designer to choose colors to be used in the design.

Requirements
Must have
• The following information is to be included:
• Miles Perrow
• Photographer
• m: 07812 593174
• e: miles@mpframeworks.co.uk
• w: mpframeworks.co.uk

```html
<!DOCTYPE html>
<html lang="en">
<head>
<meta charset="utf-8">
<title>MP Frameworks – Business Card</title>
<link href="https://fonts.googleapis.com/css2?family=Jost:wght@400;500&display=swap" rel="stylesheet">
<style>
  :root {
    --backdrop: #e6cfb6;
    --card: #f7f6f3;
    --ink: #1c1a1a;
    --muted: #6d6a68;
  }
  * { margin: 0; padding: 0; box-sizing: border-box; }
  html, body { width: 1200px; height: 1055px; overflow: hidden; }
  body {
    background: var(--backdrop);
    font-family: "Jost", "Helvetica Neue", Arial, sans-serif;
    color: var(--ink);
    display: flex;
    flex-direction: column;
    align-items: center;
    justify-content: center;
    gap: 55px;
  }
  .card {
    width: 770px;
    height: 440px;
    background: var(--card);
    position: relative;
    box-shadow: 0 6px 18px rgba(80, 55, 30, 0.18);
  }
  /* Front */
  .card-front {
    display: flex;
    align-items: center;
    justify-content: center;
    gap: 16px;
  }
  .brand-mark {
    width: 22px;
    height: 22px;
    background: var(--ink);
    flex: none;
  }
  .brand-name {
    font-size: 46px;
    font-weight: 400;
    letter-spacing: 0.12em;
    color: var(--ink);
    text-transform: uppercase;
    white-space: nowrap;
  }
  /* Back */
  .card-back {
    display: flex;
    align-items: center;
    padding-left: 110px;
    gap: 70px;
  }
  .card-back .brand-small {
    display: flex;
    align-items: center;
    gap: 9px;
  }
  .card-back .brand-small .brand-mark { width: 14px; height: 14px; }
  .card-back .brand-small .brand-name { font-size: 20px; letter-spacing: 0.1em; }
  .person-name {
    font-size: 26px;
    font-weight: 400;
    letter-spacing: 0.02em;
    text-transform: uppercase;
    line-height: 1.05;
  }
  .person-role {
    font-size: 17px;
    color: var(--muted);
    text-transform: uppercase;
    letter-spacing: 0.02em;
    margin-bottom: 14px;
  }
  .contact-list { list-style: none; }
  .contact-list li {
    display: flex;
    align-items: center;
    gap: 10px;
    font-size: 15px;
    line-height: 24px;
    white-space: nowrap;
  }
  .contact-list svg { width: 13px; height: 13px; fill: var(--ink); flex: none; }
</style>
</head>
<body>

<section class="card card-front" aria-label="Card front">
  <span class="brand-mark"></span>
  <span class="brand-name">MP Frameworks</span>
</section>

<section class="card card-back" aria-label="Card back">
  <div class="brand-small">
    <span class="brand-mark"></span>
    <span class="brand-name">MP Frameworks</span>
  </div>

  <div class="details">
    <h1 class="person-name">Miles Perrow</h1>
    <p class="person-role">Photographer</p>
    <ul class="contact-list">
      <li>
        <svg viewBox="0 0 24 24" aria-hidden="true"><path d="M6.6 10.8a15.1 15.1 0 0 0 6.6 6.6l2.2-2.2c.3-.3.7-.4 1-.2 1.1.4 2.3.6 3.6.6.6 0 1 .4 1 1V20c0 .6-.4 1-1 1C10.6 21 3 13.4 3 4c0-.6.4-1 1-1h3.5c.6 0 1 .4 1 1 0 1.3.2 2.5.6 3.6.1.3 0 .7-.2 1z"/></svg>
        07812 593174
      </li>
      <li>
        <svg viewBox="0 0 24 24" aria-hidden="true"><path d="M2 5h20v14H2zm2 2v.5l8 5 8-5V7l-8 5z"/></svg>
        miles@mpframeworks.co.uk
      </li>
      <li>
        <svg viewBox="0 0 24 24" aria-hidden="true"><path d="M12 2a10 10 0 1 0 0 20 10 10 0 0 0 0-20zm6.9 9h-3a15 15 0 0 0-1.3-5.6A8 8 0 0 1 18.9 11zM12 4.1c.9 1.3 1.8 3.6 1.9 6.9h-3.8c.1-3.3 1-5.6 1.9-6.9zM9.4 5.4A15 15 0 0 0 8.1 11h-3a8 8 0 0 1 4.3-5.6zM5.1 13h3a15 15 0 0 0 1.3 5.6A8 8 0 0 1 5.1 13zm6.9 6.9c-.9-1.3-1.8-3.6-1.9-6.9h3.8c-.1 3.3-1 5.6-1.9 6.9zm2.6-1.3a15 15 0 0 0 1.3-5.6h3a8 8 0 0 1-4.3 5.6z"/></svg>
        mpframeworks.co.uk
      </li>
    </ul>
  </div>
</section>

</body>
</html>
```